Home inspection business! professional look attracting customers just by looks. Read must haves

its a new business I started on my own for home inspections I would like something very professional to give to real estate agents and clients, its going to have my license number on it my business phone number my name my website as well etc on the back side it will be servicing areas and also what kind of services I offer I also have a business card from someone else the way I would like mine to be. I will attach my logo

Industry/Entity Type

Home Inspection

Contact Information for Business Card

listed in nice to haves

Requirements
Must have
• phone number - 718 352 9047
• website- crestwoodlatch.example
• license number #2749035186
• my name Gavin teraskovic
• picture of my logo and me on the front
• on the back of the card. stating I am servicing All of New York and Long Island
• also services I will offer will be home inspection -mold inspection -lead inspection -radon inspection -Termite Inspection -Infared Scan.
• and also we provide inspections for single family homes condos co-ops town-homes
• and commercial property
Nice to have
• same colors as the logos and also if you recommend fonts to look like the logo not sure up to you

```html
<!DOCTYPE html>
<html lang="en">
<head>
<meta charset="utf-8">
<title>Crestwood Latch Home Inspectors – Business Card</title>
<link rel="stylesheet" href="https://fonts.googleapis.com/css2?family=Montserrat:wght@500;600&family=Oswald:wght@600&family=Roboto:wght@400&display=swap">
<style>
  :root {
    --sky: #3fa6ee;
    --sky-deep: #2f8fd8;
    --slate: #6b6d70;
    --paper: #ffffff;
    --backdrop: #dcdcdc;
    --ink: #17324d;
  }
  * { box-sizing: border-box; margin: 0; padding: 0; }
  html, body { width: 1200px; height: 800px; overflow: hidden; }
  body {
    background: var(--backdrop);
    display: flex;
    align-items: center;
    justify-content: center;
    gap: 40px;
    font-family: "Montserrat", sans-serif;
  }
  .card {
    position: relative;
    width: 540px;
    height: 309px;
    border-radius: 18px;
    overflow: hidden;
  }

  /* Front */
  .card-front { background: var(--paper); }
  .front-brand {
    position: absolute;
    left: 0; right: 0; top: 0;
    height: 178px;
    display: flex;
    align-items: center;
    justify-content: center;
    gap: 18px;
  }
  .brand-dot {
    width: 56px; height: 56px;
    border-radius: 50%;
    border: 6px solid var(--slate);
  }
  .brand-name {
    font-family: "Montserrat", sans-serif;
    font-weight: 600;
    color: var(--slate);
    font-size: 26px;
    line-height: 1.15;
    letter-spacing: 1px;
    text-transform: uppercase;
  }
  .front-divider {
    position: absolute;
    left: 0; right: 0; top: 178px;
    height: 6px;
    background: var(--slate);
  }
  .front-band {
    position: absolute;
    left: 0; right: 0; top: 184px; bottom: 0;
    background: var(--sky);
    display: flex;
    align-items: center;
    justify-content: space-between;
    padding: 0 34px;
    color: var(--paper);
  }
  .holder-name {
    font-family: "Oswald", sans-serif;
    font-weight: 600;
    font-size: 30px;
    letter-spacing: 0.5px;
    text-transform: uppercase;
  }
  .contact-list {
    list-style: none;
    font-size: 12.5px;
    font-weight: 500;
    line-height: 1.6;
    text-transform: uppercase;
  }

  /* Back */
  .card-back {
    background: var(--sky);
    display: flex;
    flex-direction: column;
    align-items: center;
    justify-content: center;
    padding: 0 36px;
    text-align: center;
  }
  .back-brand {
    display: flex;
    align-items: center;
    gap: 14px;
    margin-bottom: 22px;
  }
  .back-brand .brand-dot { border-color: var(--sky-deep); width: 46px; height: 46px; border-width: 5px; }
  .back-brand .brand-name { color: var(--sky-deep); font-size: 22px; }
  .service-notes {
    font-family: "Roboto", sans-serif;
    font-weight: 400;
    color: var(--ink);
    font-size: 12.5px;
    line-height: 1.45;
  }
</style>
</head>
<body>
  <section class="card card-front">
    <div class="front-brand">
      <span class="brand-dot"></span>
      <p class="brand-name">Crestwood Latch<br>Home Inspectors</p>
    </div>
    <div class="front-divider"></div>
    <div class="front-band">
      <h1 class="holder-name">Gavin Teraskovic</h1>
      <ul class="contact-list">
        <li>718 352 9047</li>
        <li>www.crestwoodlatch.example</li>
        <li>License No #2749035186</li>
      </ul>
    </div>
  </section>

  <section class="card card-back">
    <div class="back-brand">
      <span class="brand-dot"></span>
      <p class="brand-name">Crestwood Latch<br>Home Inspectors</p>
    </div>
    <p class="service-notes">
      I am servicing All of New York and Long Island also services I will offer will be<br>
      Home inspection | Mold inspection | Lead inspection | Radon inspection<br>
      Termite Inspection | Infared Scan.<br>
      And also we provide inspections for single family homes condos<br>
      co-ops town-homes &amp; commercial property
    </p>
  </section>
</body>
</html>
```